Calderwell Homes

To produce a business card design for our newly established house building and development company, We have had a logo design done please see attached, our slogan is "Crafting the homes you love"
Contact Information for Business Card
Adress on card needs to Read - 47 Hollowmere Lane, Marsford, Wendlebyshire NN14 3QX. Director name Mark Ellery
Requirements
Must have
- Web adress is www.calderwell-homes.co.uk
- Email address is info@calderwell-homes.co.uk
- phone number 07700 900418

```html
<!DOCTYPE html>
<html lang="en">
<head>
<meta charset="utf-8">
<title>Calderwell Homes – Business Card</title>
<link rel="stylesheet" href="https://fonts.googleapis.com/css2?family=Work+Sans:wght@400;500;700&display=swap">
<style>
  :root {
    --bg: #2b2b2b;
    --card: #1d1d1d;
    --card-edge: #242424;
    --green: #7cc623;
    --grey: #9a9a9a;
    --white: #f2f2f2;
  }
  * { margin: 0; padding: 0; box-sizing: border-box; }
  html, body { width: 1200px; height: 900px; overflow: hidden; }
  body {
    background: var(--bg);
    font-family: "Work Sans", Arial, sans-serif;
    display: flex;
    flex-direction: column;
    align-items: center;
    justify-content: center;
    gap: 34px;
  }
  .card {
    position: relative;
    width: 700px;
    height: 400px;
    background: linear-gradient(135deg, var(--card-edge), var(--card));
    overflow: hidden;
  }
  .card::after {
    content: "";
    position: absolute;
    left: 0; right: 0; bottom: 0;
    height: 7px;
    background: var(--green);
  }
  .brand {
    display: flex;
    flex-direction: column;
    align-items: center;
  }
  .brand-name {
    color: var(--green);
    font-weight: 700;
    font-size: 40px;
    letter-spacing: 2px;
    text-transform: uppercase;
    display: flex;
    align-items: center;
    gap: 14px;
    white-space: nowrap;
  }
  .brand-mark {
    width: 18px; height: 18px;
    background: var(--green);
    flex-shrink: 0;
  }
  .brand-rule {
    width: 100%;
    height: 2px;
    background: var(--grey);
    margin: 12px 0 8px;
  }
  .brand-tagline {
    color: var(--green);
    font-size: 10px;
    letter-spacing: 5px;
    text-transform: uppercase;
    white-space: nowrap;
  }
  /* Front */
  .card-front {
    display: flex;
    align-items: center;
    justify-content: center;
    padding-bottom: 40px;
  }
  /* Back */
  .card-back {
    display: flex;
    align-items: center;
    padding: 0 24px 10px 30px;
  }
  .card-back .brand { width: 290px; flex-shrink: 0; }
  .card-back .brand-name { font-size: 22px; gap: 8px; letter-spacing: 1px; }
  .card-back .brand-mark { width: 11px; height: 11px; }
  .card-back .brand-rule { margin: 9px 0 6px; }
  .card-back .brand-tagline { font-size: 7.5px; letter-spacing: 3px; }
  .divider {
    width: 3px;
    height: 250px;
    background: var(--green);
    margin: 0 26px;
    flex-shrink: 0;
  }
  .contact { color: var(--white); white-space: nowrap; }
  .contact-name {
    color: var(--green);
    font-weight: 700;
    font-size: 26px;
    text-transform: uppercase;
    letter-spacing: 1px;
    line-height: 1.1;
  }
  .contact-role { font-size: 15px; margin-bottom: 14px; }
  .contact-address { font-size: 15px; line-height: 1.4; margin-bottom: 8px; }
  .contact-list { list-style: none; }
  .contact-list li {
    display: flex;
    align-items: center;
    gap: 10px;
    font-size: 15px;
    line-height: 1.5;
  }
  .contact-list svg { width: 12px; height: 12px; flex-shrink: 0; }
</style>
</head>
<body>

  <section class="card card-front">
    <div class="brand">
      <div class="brand-name"><span class="brand-mark"></span>Calderwell Homes</div>
      <div class="brand-rule"></div>
      <div class="brand-tagline">Crafting the homes you love</div>
    </div>
  </section>

  <section class="card card-back">
    <div class="brand">
      <div class="brand-name"><span class="brand-mark"></span>Calderwell Homes</div>
      <div class="brand-rule"></div>
      <div class="brand-tagline">Crafting the homes you love</div>
    </div>

    <div class="divider"></div>

    <div class="contact">
      <h1 class="contact-name">Mark Ellery</h1>
      <p class="contact-role">Director</p>
      <p class="contact-address">47 Hollowmere Lane, Marsford,<br>Wendlebyshire NN14 3QX.</p>
      <ul class="contact-list">
        <li>
          <svg viewBox="0 0 12 12" aria-hidden="true"><rect x="3" y="0.5" width="6" height="11" rx="1" fill="none" stroke="#7cc623" stroke-width="1.2"/><circle cx="6" cy="9.5" r="0.7" fill="#7cc623"/></svg>
          07700 900418
        </li>
        <li>
          <svg viewBox="0 0 12 12" aria-hidden="true"><path d="M2.5 1 L4.5 1 L5.2 3.6 L3.9 4.6 C4.6 6.2 5.8 7.4 7.4 8.1 L8.4 6.8 L11 7.5 L11 9.5 C11 10.3 10.3 11 9.5 11 C5 11 1 7 1 2.5 C1 1.7 1.7 1 2.5 1 Z" fill="#7cc623"/></svg>
          07700 900527
        </li>
        <li>
          <svg viewBox="0 0 12 12" aria-hidden="true"><rect x="0.8" y="2.2" width="10.4" height="7.6" fill="none" stroke="#7cc623" stroke-width="1.2"/><path d="M0.8 2.4 L6 6.4 L11.2 2.4" fill="none" stroke="#7cc623" stroke-width="1.2"/></svg>
          info@calderwell-homes.co.uk
        </li>
        <li>
          <svg viewBox="0 0 12 12" aria-hidden="true"><circle cx="6" cy="6" r="5.2" fill="none" stroke="#7cc623" stroke-width="1.1"/><ellipse cx="6" cy="6" rx="2.3" ry="5.2" fill="none" stroke="#7cc623" stroke-width="1"/><line x1="0.8" y1="6" x2="11.2" y2="6" stroke="#7cc623" stroke-width="1"/></svg>
          www.calderwell-homes.co.uk
        </li>
      </ul>
    </div>
  </section>

</body>
</html>
```